Fireworks company

COLORFUL design, incorporating logo (attached).
Information to be included:
PO BOX 4829
Marlow Vale 3891
Ph 03 5461 8237
Fax 03 5387 9216
Email sales@brindarockets.com.au
Web www.brindarockets.com.au

Check out our website for more inspiration? :-)

```html
<!DOCTYPE html>
<html lang="en">
<head>
<meta charset="utf-8">
<title>Brinda Rockets Letterhead</title>
<link rel="stylesheet" href="https://fonts.googleapis.com/css2?family=Open+Sans:wght@400;700&display=swap">
<style>
  :root {
    --backdrop: #6e6e6e;
    --paper: #ffffff;
    --ink-black: #0b0b0b;
    --spark-orange: #f08a1c;
    --spark-gold: #f5c333;
    --text-light: #ffffff;
    --watermark: #f8e0d6;
  }
  * { margin: 0; padding: 0; box-sizing: border-box; }
  html, body {
    width: 1200px; height: 1000px; overflow: hidden;
    background: var(--backdrop);
    font-family: "Open Sans", Arial, sans-serif;
  }
  .letterhead {
    position: absolute; left: 258px; top: 58px;
    width: 684px; height: 885px;
    background: var(--paper);
    overflow: hidden;
  }
  .header-band { position: absolute; left: 0; top: 0; width: 684px; height: 150px; }
  .burst {
    position: absolute;
  }
  .burst--left {
    left: 0; top: 0; width: 72px; height: 62px;
    background: radial-gradient(circle at 40% 45%, #ffd24a 0%, #f07a1a 35%, rgba(200,60,20,.5) 60%, rgba(11,11,11,0) 75%);
  }
  .burst--right {
    left: 505px; top: 0; width: 179px; height: 100px;
    background:
      radial-gradient(circle at 22% 40%, #e8f04a 0%, #9cc020 22%, rgba(11,11,11,0) 42%),
      radial-gradient(circle at 55% 55%, #ffb347 0%, #f06a18 26%, rgba(11,11,11,0) 48%),
      radial-gradient(circle at 85% 20%, #d8ecff 0%, #6aa6e0 18%, rgba(11,11,11,0) 36%);
  }
  .brand {
    position: absolute; left: 66px; top: 30px;
    display: flex; align-items: center; gap: 10px;
  }
  .brand-name {
    color: var(--text-light);
    font-weight: 700; font-size: 21px; line-height: 1.1;
    letter-spacing: 1px; text-transform: uppercase;
  }
  .brand-dot {
    width: 14px; height: 14px; border-radius: 50%;
    background: var(--spark-gold);
  }
  .contact-list { list-style: none; position: absolute; top: 26px; left: 0; }
  .contact-item {
    position: absolute; white-space: nowrap;
    display: flex; align-items: center; gap: 8px;
    color: var(--text-light); font-size: 9px; line-height: 12px;
  }
  .contact-icon {
    width: 9px; height: 9px; border-radius: 2px;
    background: var(--spark-orange); display: block;
  }
  .watermark {
    position: absolute; left: 165px; top: 485px;
    display: flex; align-items: center; gap: 14px;
  }
  .watermark-name {
    color: var(--watermark); font-weight: 700;
    font-size: 46px; line-height: 1.05; letter-spacing: 2px;
    text-transform: uppercase;
  }
  .watermark-dot {
    width: 40px; height: 40px; border-radius: 50%;
    background: var(--watermark);
  }
  .footer-band { position: absolute; left: 0; bottom: 0; width: 684px; height: 13px; }
</style>
</head>
<body>
  <main class="letterhead">
    <svg class="header-band" viewBox="0 0 684 150" aria-hidden="true">
      <path d="M0 0 H684 V108 C600 106 420 102 240 112 C140 118 60 128 0 142 Z" fill="var(--ink-black)"/>
      <line x1="316" y1="0" x2="368" y2="104" stroke="var(--spark-orange)" stroke-width="2.5"/>
    </svg>

    <div class="burst burst--left" role="img" aria-label="Firework burst illustration"></div>
    <div class="burst burst--right" role="img" aria-label="Cluster of colourful firework bursts"></div>

    <div class="brand">
      <span class="brand-name">Brinda<br>Rockets</span>
      <span class="brand-dot"></span>
    </div>

    <ul class="contact-list">
      <li class="contact-item" style="left:358px; top:0;"><span class="contact-icon"></span>03 5461 8237</li>
      <li class="contact-item" style="left:366px; top:15px;"><span class="contact-icon"></span>03 5387 9216</li>
      <li class="contact-item" style="left:374px; top:30px;"><span class="contact-icon"></span>sales@brindarockets.com.au</li>
      <li class="contact-item" style="left:382px; top:45px;"><span class="contact-icon"></span>www.brindarockets.com.au</li>
      <li class="contact-item" style="left:392px; top:60px;"><span class="contact-icon"></span>PO BOX 4829, Marlow Vale 3891</li>
    </ul>

    <div class="watermark" aria-hidden="true">
      <span class="watermark-name">Brinda<br>Rockets</span>
      <span class="watermark-dot"></span>
    </div>

    <svg class="footer-band" viewBox="0 0 684 13" aria-hidden="true">
      <rect width="684" height="13" fill="var(--ink-black)"/>
      <line x1="336" y1="0" x2="344" y2="13" stroke="var(--spark-orange)" stroke-width="2"/>
    </svg>
  </main>
</body>
</html>
```